Desserts Business Card Design

I own a dessert business and cakes and cupcakes are my biggest sellers. I have been running this as a part time business since 2007. I am now looking to expand going full time and open a store front within he next 12 months.
With this expansion I am looking to have my own design setup for the business.

I have been using a design on my cards provided to me by a website I got the cards from. I would like a more original design I can use for the cards, the store front and any other advertising I will be doing. I also have a saying on the back of my business card which I would like to be worked in as well.
"Baked fresh each day, with love in every bite"

Target Market(s)

Younger and older families of all ethnic backgrounds

Industry/Entity Type

Advertising

Contact Information for Business Card

Maribel's Sugared Treats
Tobias Fenwick
4417 Pinecrest Terrace
Millbrook, Ontario
M3P 7J2

Logo Text

Logo styles of interest
Emblem Logo
Pictorial/Combination Logo
Wordmark Logo
Lettermark Logo
Requirements
Must have
• "Baked fresh each day, with love in every bite"
Nice to have
• Maribel's Sugared Treats - This can actually be turned into a logo which is really what I am looking for. Using MST, converted to a logo? I am really looking to see what you can provide me with.
A cake or cupcake added on the front of the card?
Should not have
• I cannot think of anything right now. I an looking forward to see the imaginations from the design groups

```html
<!DOCTYPE html>
<html lang="en">
<head>
<meta charset="utf-8">
<title>Maribel's Sugared Treats – Business Card</title>
<link rel="stylesheet" href="https://fonts.googleapis.com/css2?family=Open+Sans:wght@700&family=PT+Sans+Narrow:wght@700&display=swap">
<style>
  :root {
    --magenta: #d9088c;
    --cream: #faeed0;
    --frosting: #f6a9b5;
    --wrapper-dark: #a80068;
    --white: #ffffff;
    --backdrop: #e8e8e8;
  }
  html, body {
    margin: 0;
    width: 992px;
    height: 1200px;
    overflow: hidden;
    background: var(--backdrop);
    font-family: "Open Sans", Arial, sans-serif;
    font-weight: 700;
  }
  .card {
    position: absolute;
    left: 89px;
    width: 818px;
    height: 486px;
    border-radius: 16px;
    overflow: hidden;
    background: var(--magenta);
    box-shadow: 0 6px 14px rgba(0,0,0,0.28);
  }
  .card--front { top: 75px; }
  .card--back { top: 635px; }
  .card__bg { position: absolute; inset: 0; }
  .card__text { position: absolute; margin: 0; color: var(--white); white-space: nowrap; font-weight: 700; }

  .holder-name { left: 47px; top: 22px; font-size: 32px; }
  .address { left: 47px; top: 355px; font-size: 24px; line-height: 36px; }
  .email { left: 47px; top: 434px; font-size: 16px; }

  .monogram {
    position: absolute;
    display: flex; align-items: center; justify-content: center;
    border-radius: 50%;
    background: var(--cream);
    border: 4px solid var(--magenta);
    color: var(--magenta);
    font-weight: 700;
  }
  .card--front .monogram { left: 197px; top: 100px; width: 78px; height: 78px; font-size: 25px; }
  .card--back .monogram { left: 612px; top: 28px; width: 78px; height: 78px; font-size: 25px; border-color: var(--white); }

  .business-name {
    position: absolute; left: 30px; top: 192px; width: 440px;
    margin: 0; color: var(--magenta); font-weight: 700;
    font-size: 44px; line-height: 54px; text-align: center;
  }

  .illustration {
    position: absolute;
    border-radius: 46% 46% 30% 30%;
    background: linear-gradient(180deg, var(--frosting) 0%, var(--cream) 45%, var(--magenta) 60%, var(--wrapper-dark) 100%);
  }
  .card--front .illustration { left: 490px; top: 40px; width: 296px; height: 352px; }
  .card--back .illustration { left: 39px; top: 244px; width: 194px; height: 209px; }

  .website { right: 30px; top: 128px; font-size: 17px; }
  .phone { right: 30px; top: 356px; font-size: 17px; }
  .motto {
    position: absolute; left: 39px; top: 170px; width: 760px; margin: 0;
    font-family: "PT Sans Narrow", "Arial Narrow", sans-serif; font-weight: 700;
    color: var(--magenta); font-size: 58px; line-height: 74px;
  }
  .motto__line { display: block; }
  .motto__line--second { text-align: right; padding-right: 28px; }
</style>
</head>
<body>
  <section class="card card--front">
    <svg class="card__bg" width="818" height="486" viewBox="0 0 818 486" aria-hidden="true">
      <rect x="0" y="107" width="818" height="231" fill="var(--cream)"/>
      <clipPath id="front-clip"><rect x="0" y="0" width="794" height="486"/></clipPath>
      <circle cx="707" cy="243" r="249" fill="var(--cream)" clip-path="url(#front-clip)"/>
    </svg>
    <p class="card__text holder-name">Tobias Fenwick</p>
    <div class="monogram">MST</div>
    <p class="business-name">Maribel's<br>Sugared Treats</p>
    <p class="card__text address">4417 Pinecrest Terrace<br>Millbrook, Ontario M3P 7J2</p>
    <p class="card__text email">Sweet.hello@maribelstreats.com</p>
    <div class="illustration" role="img" aria-label="Cartoon cupcake with pink frosting and a cherry on top"></div>
  </section>

  <section class="card card--back">
    <svg class="card__bg" width="818" height="486" viewBox="0 0 818 486" aria-hidden="true">
      <rect x="0" y="155" width="818" height="188" fill="var(--cream)"/>
    </svg>
    <div class="monogram">MST</div>
    <p class="card__text website">www.maribelstreats.com</p>
    <p class="motto">
      <span class="motto__line">"Baked fresh each day,</span>
      <span class="motto__line motto__line--second">with love in every bite"</span>
    </p>
    <p class="card__text phone">Call : 555-301-4782</p>
    <div class="illustration" role="img" aria-label="Cartoon cupcake with pink frosting and a cherry on top"></div>
  </section>
</body>
</html>
```